Steady Path Physical Therapy and Wellness brochure

We need a trifold brochure that would go out to physicians. I am marketing to them to get patient referrals. My business name is Steady Path Physical Therapy and Wellness, PC. We specialize in treating balance and dizziness and other neurological disorders as well as in providing general physical therapy services. We could use a logo of some sort on the brochure. Please go to steadypathpt.example and look at the about page. My business does seminars too, but I want this brochure geared to the physical therapy services we provide. The business card I attached has important information and the phone and fax number. My address is:
48207 Harlow Ridge Road, Suite #214
Harbor Vista, CA 92640
I would like information on my business, but please include my name also. I am the sole physical therapist of the practice, but want to give the impression I am not just a small operation. I need the brochure to have Steady Path Physical Therapy and Wellness as the title, but information on me as the owner. I attached the brochure for some ideas. This is the one for my seminars. I don't want the new one geared toward seminars or this busy. However, the brochure does have some idea, like the graphic of the inner ear and then some information on me.
Thanks,
Updates
Project Deadline Extended Reason: Oh my gosh, I thought my deadline was May 13 and wanted to extend it beyond that. Can you please clarify what my deadlne is?I am new to this. Most of the designers have done something a bit different that I originally wanted.Perhaps due to language differences, this happened. However, I am liking what they have done.Please extend my deadline. I am a sole business owner.Thanks, Marla Added Wednesday, May 4, 2016
Target Market(s)
Physicians and perhaps patients
Industry/Entity Type
Business
Requirements
Must have
- My business name, my name, phone and fax, address, my picture, an about section. Not overly busy. I work with people with balance problems.
- Please state I accept Medicare Insurance. Below is on the about section.
- Doctor of Physical Therapy
- Board Certified Geriatric Specialist
- KRQP Certified for Parkinson's treatment
- Vestibular Specialist
Nice to have
- all the above. please look at my website "about section"
- It's maybe okay to mention I am a part-time University professor, but maybe not too much on this.
Should not have
- not to busy, I attached an example of a trifold brochure since it has information on me, but I don't want something this busy.

```html
<!DOCTYPE html>
<html lang="en">
<head>
<meta charset="utf-8">
<title>Steady Path Physical Therapy and Wellness – Trifold Brochure</title>
<link rel="stylesheet" href="https://fonts.googleapis.com/css2?family=Lato:wght@400;700&family=Montserrat:wght@700;800&display=swap">
<style>
  :root {
    --page-bg: #e9e6e2;
    --blue-deep: #1d5fa8;
    --blue-mid: #2f7cc4;
    --blue-bright: #2fb4ea;
    --blue-light: #8fd3f3;
    --grey-light: #f1f1f1;
    --grey-mid: #c9c9c9;
    --charcoal: #333333;
    --white: #ffffff;
    --ink: #1e1e1e;
    --title: #e9edf1;
  }
  html, body {
    margin: 0; padding: 0;
    width: 1200px; height: 907px;
    overflow: hidden;
    background: var(--page-bg);
  }
  .canvas { position: relative; width: 1200px; height: 907px; }
  .brochure {
    position: absolute; left: 77px; top: 70px;
    width: 1043px; height: 742px;
    overflow: hidden;
    box-shadow: 0 6px 18px rgba(0,0,0,.25);
    background: var(--blue-deep);
  }
  .photo { position: absolute; }
  .photo--owner {
    left: 0; top: 0; width: 348px; height: 370px;
    background: linear-gradient(160deg, #e7e6e2 0%, #cfcac2 45%, #5a5550 100%);
  }
  .photo--therapy {
    left: 348px; top: 0; width: 350px; height: 560px;
    background: linear-gradient(170deg, #8d5a3a 0%, #c8b39c 40%, #9fc9b0 60%, #7aa6c9 100%);
  }
  .photo--stones {
    left: 698px; top: 60px; width: 345px; height: 520px;
    background: radial-gradient(ellipse at 60% 55%, #d9c7a6 0%, #b59c78 28%, #3f8fb8 60%, #1b6e9f 100%);
  }
  .waves { position: absolute; left: 0; top: 0; width: 1043px; height: 742px; }

  .about-pill {
    position: absolute; left: 155px; top: 285px;
    width: 140px; height: 48px;
    border-radius: 0 24px 24px 0;
    background: var(--blue-bright);
    box-shadow: 0 2px 6px rgba(0,0,0,.3);
    font: 800 26px/48px "Montserrat", sans-serif;
    color: var(--white); text-align: center;
  }
  .about-copy {
    position: absolute; left: 16px; top: 367px; width: 322px;
    font: 400 13.6px/17.6px "Lato", sans-serif;
    color: var(--white); text-align: justify;
  }
  .about-copy p { margin: 0 0 17.6px; }

  .contact {
    position: absolute; left: 348px; top: 530px; width: 350px;
    text-align: center; font-family: "Lato", sans-serif; color: var(--ink);
  }
  .brand-mark {
    display: inline-flex; align-items: center; gap: 6px;
    font: 700 15px/20px "Lato", sans-serif; color: var(--charcoal);
    margin-bottom: 16px;
  }
  .brand-mark .dot { width: 12px; height: 12px; border-radius: 50%; background: var(--charcoal); }
  .contact .practice { font-weight: 700; font-size: 11.5px; margin: 0; }
  .contact p { margin: 0; font-size: 12px; line-height: 15px; }
  .contact .line { display: flex; justify-content: center; align-items: center; gap: 6px; }
  .contact .gap { margin-top: 8px; }
  .contact svg { width: 10px; height: 10px; fill: var(--ink); }

  .cover-mark {
    position: absolute; left: 728px; top: 48px;
    display: flex; align-items: center; gap: 8px;
    font: 700 20px/24px "Lato", sans-serif; color: var(--white);
  }
  .cover-mark .dot { width: 14px; height: 14px; border-radius: 50%; background: var(--white); }
  .cover-title {
    position: absolute; left: 698px; top: 612px; width: 345px;
    margin: 0; text-align: center;
    font: 800 25px/32px "Montserrat", sans-serif;
    color: var(--title); letter-spacing: .5px;
    text-shadow: 0 2px 3px rgba(0,0,0,.35);
  }
</style>
</head>
<body>
<div class="canvas">
  <article class="brochure">
    <div class="photo photo--owner" role="img" aria-label="Portrait photo of the practice owner seated at a desk in a dark blazer"></div>
    <div class="photo photo--therapy" role="img" aria-label="Photo of a therapist guiding an older patient walking between parallel bars"></div>
    <div class="photo photo--stones" role="img" aria-label="Photo of balanced stacked pebbles against a blue sea"></div>

    <svg class="waves" viewBox="0 0 1043 742" aria-hidden="true">
      <defs>
        <linearGradient id="panelBlue" x1="0" y1="0" x2="1" y2="1">
          <stop offset="0" stop-color="#2a78c0"/>
          <stop offset="1" stop-color="#174f95"/>
        </linearGradient>
        <linearGradient id="panelGrey" x1="0" y1="0" x2="1" y2="0">
          <stop offset="0" stop-color="#d6d6d6"/>
          <stop offset=".5" stop-color="#f4f4f4"/>
          <stop offset="1" stop-color="#cfcfcf"/>
        </linearGradient>
        <linearGradient id="coverBlue" x1="0" y1="0" x2="1" y2="0">
          <stop offset="0" stop-color="#1f7fc0"/>
          <stop offset=".5" stop-color="#3aa2dc"/>
          <stop offset="1" stop-color="#1f7fc0"/>
        </linearGradient>
      </defs>
      <path d="M0,352 C110,348 220,285 348,212 L348,742 L0,742 Z" fill="url(#panelBlue)"/>
      <path d="M0,340 C110,336 220,270 348,198" fill="none" stroke="#ffffff" stroke-width="10"/>
      <path d="M0,326 C110,322 220,255 348,184" fill="none" stroke="#2fb4ea" stroke-width="16"/>
      <path d="M348,530 C470,520 600,400 698,272 L698,742 L348,742 Z" fill="url(#panelGrey)"/>
      <path d="M348,516 C470,506 600,386 698,258" fill="none" stroke="#ffffff" stroke-width="10"/>
      <path d="M348,500 C470,490 600,370 698,242" fill="none" stroke="#2fb4ea" stroke-width="18"/>
      <path d="M698,0 L1043,0 L1043,70 C910,58 790,140 698,232 Z" fill="url(#coverBlue)"/>
      <path d="M698,242 C790,150 910,66 1043,80" fill="none" stroke="#ffffff" stroke-width="8"/>
      <path d="M698,236 C790,144 910,60 1043,74" fill="none" stroke="#8fd3f3" stroke-width="6"/>
      <path d="M698,560 C810,565 960,480 1043,395 L1043,742 L698,742 Z" fill="url(#coverBlue)"/>
      <path d="M760,552 C880,530 990,440 1043,330" fill="none" stroke="#333333" stroke-width="22"/>
      <path d="M698,556 C810,561 960,476 1043,392" fill="none" stroke="#ffffff" stroke-width="12"/>
      <line x1="348" y1="0" x2="348" y2="742" stroke="rgba(0,0,0,.12)" stroke-width="1"/>
      <line x1="698" y1="0" x2="698" y2="742" stroke="rgba(0,0,0,.15)" stroke-width="1"/>
    </svg>

    <section class="panel-about">
      <div class="about-pill">ABOUT</div>
      <div class="about-copy">
        <p>Steady Path Physical Therapy and Wellness, Professional Corporation offers physical therapy care with a focus on dizziness, vestibular and balance recovery. Marla Kessler PT, DPT, GCS founded the practice and leads it as President and Director. Her clinical work centers on inner ear disorders, eye movement control, fall prevention and recovery after concussion. She has practiced in dedicated balance and dizziness clinics and has treated patients in outpatient settings, rehabilitation units, hospitals, skilled nursing and home care, bringing a calm, patient-centered approach to every visit.</p>
        <p>Earlier in her career she served as a vestibular physical therapist for a military medical center, helping service members recover from head injuries. Today she pairs that depth of experience with board certification in geriatrics and Medicare-accepted care, and she also teaches part-time at a local university.</p>
      </div>
    </section>

    <section class="contact">
      <div class="brand-mark"><span class="dot"></span>Steady Path</div>
      <p class="practice">Steady Path Physical Therapy and Wellness, PC</p>
      <p class="line"><svg viewBox="0 0 10 10"><path d="M5 0a3.5 3.5 0 0 0-3.5 3.5C1.5 6 5 10 5 10s3.5-4 3.5-6.5A3.5 3.5 0 0 0 5 0zm0 5a1.5 1.5 0 1 1 0-3 1.5 1.5 0 0 1 0 3z"/></svg>48207 Harlow Ridge Road, Suite #214</p>
      <p>Harbor Vista, CA 92640</p>
      <p class="line gap"><svg viewBox="0 0 10 10"><path d="M0 2h10v6H0z M0 2l5 3.5L10 2" fill="none" stroke="#1e1e1e" stroke-width="1"/></svg>marlakesslerdpt@example.com</p>
      <p class="line gap"><svg viewBox="0 0 10 10"><path d="M2.5 0.5 4 3 3 4c.6 1.3 1.7 2.4 3 3l1-1 2.5 1.5-1 2C4.5 9.5.5 5.5.5 1.5z"/></svg>(949) 555-0142</p>
      <p class="line gap"><svg viewBox="0 0 10 10"><path d="M0 3c2-2 8-2 10 0L8.5 4.5 7 3.5V2.5H3v1L1.5 4.5z M1.5 5h7l1 4h-9z"/></svg>(844) 555-0187</p>
    </section>

    <section class="panel-cover">
      <div class="cover-mark"><span class="dot"></span>Steady Path</div>
      <h1 class="cover-title">STEADY PATH<br>PHYSICAL THERAPY<br>&amp; WELLNESS</h1>
    </section>
  </article>
</div>
</body>
</html>
```